Stump Grinding sidewalk sign

I have an A-frame sign that has a 24" x 36" flat area for a vinyl sign to be applied to. the sign can also be applied to sheet metal and then screwed to the A-frame sign.
I have included a few pictures of my logo, the A-frame, and my business card.

Target Market(s)

Tree and stump industry

Font styles to use
Decorative

Requirements
Must have
• I would like my company name , logo, slogan, and phone number on the sign. Along with "Fully Insured" and "free Estimates".
The sign is black, and I would like bright colors such as safety green and/or neon yellow. Or possibly a florescent red?
Nice to have
• Some sort of background to break up the blank "solidness"

```html
<!DOCTYPE html>
<html lang="en">
<head>
<meta charset="UTF-8">
<title>Marlow's Stump Grinding – Sidewalk Sign</title>
<link href="https://fonts.googleapis.com/css2?family=Cinzel:wght@500;600&family=Libre+Baskerville:wght@700&family=Oswald:wght@700&family=Montserrat:wght@800&display=swap" rel="stylesheet">
<style>
  :root {
    --backdrop: #2b2b2b;
    --green-light: #9ed64a;
    --green-mid: #5fb52a;
    --green-deep: #2f8a1c;
    --green-ink: #1e6b1a;
    --white: #ffffff;
    --photo-grass: #6f9a3a;
    --photo-soil: #b89a6e;
    --photo-machine: #d9a21c;
  }
  * { margin: 0; padding: 0; box-sizing: border-box; }
  html, body { width: 868px; height: 1200px; overflow: hidden; background: var(--backdrop); }
  .sign {
    position: absolute; left: 44px; top: 15px;
    width: 780px; height: 1170px; overflow: hidden;
    background: linear-gradient(180deg, var(--green-light) 0%, var(--green-mid) 60%, var(--green-deep) 100%);
  }
  .sign-header {
    position: absolute; left: 0; top: 0; width: 780px; height: 330px;
  }
  .brand-mark {
    position: absolute; left: 92px; top: 70px;
    width: 140px; height: 140px; border-radius: 50%;
    background: var(--white);
  }
  .brand-name {
    position: absolute; left: 262px; top: 80px; width: 480px;
    font-family: "Cinzel", serif; font-weight: 600;
    color: var(--white); font-size: 78px; line-height: 1; white-space: nowrap;
  }
  .brand-tagline {
    position: absolute; left: 264px; top: 176px; width: 480px;
    font-family: "Cinzel", serif; font-weight: 600;
    color: var(--white); font-size: 42px; letter-spacing: 1px; line-height: 1; white-space: nowrap;
  }
  .hero-photo {
    position: absolute; left: 0; top: 290px; width: 780px; height: 609px;
    background:
      radial-gradient(ellipse 45% 32% at 78% 22%, var(--photo-machine) 0%, rgba(217,162,28,0) 70%),
      radial-gradient(ellipse 55% 28% at 72% 48%, var(--photo-soil) 0%, rgba(184,154,110,0) 75%),
      linear-gradient(180deg, #4d6e2c 0%, var(--photo-grass) 40%, var(--green-light) 75%, #8cce43 100%);
  }
  .slogan {
    position: absolute; left: 87px; top: 722px;
    font-family: "Libre Baskerville", serif; font-weight: 700;
    color: var(--green-ink); font-size: 68px; line-height: 86px; white-space: nowrap;
  }
  .call-band {
    position: absolute; left: 0; top: 899px; width: 780px; height: 104px;
    background: linear-gradient(90deg, var(--white) 70%, rgba(255,255,255,0.85) 100%);
  }
  .call-number {
    position: absolute; left: 87px; top: 4px;
    font-family: "Oswald", sans-serif; font-weight: 700;
    color: var(--green-deep); font-size: 80px; line-height: 96px; white-space: nowrap;
  }
  .assurances {
    position: absolute; left: 0; top: 1003px; width: 780px; height: 167px;
    background: linear-gradient(180deg, var(--green-mid) 0%, var(--green-deep) 100%);
  }
  .assurance {
    position: absolute; top: 40px; display: flex; align-items: center; gap: 16px;
  }
  .assurance svg { width: 68px; height: 68px; }
  .assurance-text {
    font-family: "Montserrat", sans-serif; font-weight: 800;
    color: var(--white); font-size: 38px; line-height: 40px;
  }
</style>
</head>
<body>
  <div class="sign">
    <div class="hero-photo" role="img" aria-label="Photo of a stump grinder chewing a tree stump into wood chips on a green lawn"></div>

    <svg class="sign-header" viewBox="0 0 780 330" aria-hidden="true">
      <defs>
        <linearGradient id="headerFill" x1="0" y1="0" x2="1" y2="0">
          <stop offset="0" stop-color="#3f9a22"/>
          <stop offset="0.5" stop-color="#7cc23a"/>
          <stop offset="1" stop-color="#3f9a22"/>
        </linearGradient>
      </defs>
      <path d="M0 0 H780 V255 Q390 330 0 265 Z" fill="url(#headerFill)"/>
      <path d="M0 265 Q390 330 780 255 V285 Q390 355 0 300 Z" fill="#ffffff"/>
    </svg>
    <div class="brand-mark"></div>
    <div class="brand-name">MARLOW'S</div>
    <div class="brand-tagline">STUMP GRINDING</div>

    <div class="slogan">NO STUMP,<br>TOO PLUMP</div>

    <div class="call-band">
      <div class="call-number">CALL: 555-204-7731</div>
    </div>

    <div class="assurances">
      <div class="assurance" style="left:60px;">
        <svg viewBox="0 0 68 68" aria-hidden="true">
          <circle cx="34" cy="34" r="30" fill="#ffffff"/>
          <circle cx="34" cy="34" r="23" fill="#2f8a1c"/>
          <path d="M22 35 L31 44 L48 25" fill="none" stroke="#ffffff" stroke-width="7" stroke-linecap="round" stroke-linejoin="round"/>
        </svg>
        <div class="assurance-text">FULLY<br>INSURED</div>
      </div>
      <div class="assurance" style="left:395px;">
        <svg viewBox="0 0 68 68" aria-hidden="true">
          <circle cx="34" cy="34" r="30" fill="#ffffff"/>
          <circle cx="34" cy="34" r="23" fill="#2f8a1c"/>
          <path d="M22 35 L31 44 L48 25" fill="none" stroke="#ffffff" stroke-width="7" stroke-linecap="round" stroke-linejoin="round"/>
        </svg>
        <div class="assurance-text">FREE<br>ESTIMATES</div>
      </div>
    </div>
  </div>
</body>
</html>
```